We need a flyer for a mail action to attract people's attention and to get new items for sale. We would like to focus on a kind of full service package, where a complete package should be advertised from a single source. Clearing out, sale guarantee, increase in value through renovation when accessing own craftsmen, home staging, etc. The flyer should be as possible to point out the benefits for the customer to have to take care of yourself. The design should be simple, elegant, yet down-to-earth and match the design and colors of the existing logo. The slogan "We Love Real Estate" should be incorporated as much as possible

please in German

We need the flyer in German please

```html
<!DOCTYPE html>
<html lang="de">
<head>
<meta charset="utf-8">
<title>NORDHAUS – Rundum-Service Postkarte</title>
<link rel="stylesheet" href="https://fonts.googleapis.com/css2?family=Kanit:wght@500&family=Libre+Baskerville:wght@400;700&family=Tinos:wght@400;700&family=Yanone+Kaffeesatz:wght@400&display=swap">
<style>
  :root {
    --stage: #e4e5e8;
    --royal: #0c0cc4;
    --royal-deep: #07077a;
    --navy: #0b0b8e;
    --ink: #1b1b1f;
    --band: #2a2829;
    --paper: #ffffff;
    --rule: #cfcfd4;
  }
  html, body {
    margin: 0;
    padding: 0;
    width: 876px;
    height: 1200px;
    overflow: hidden;
    background: var(--stage);
  }
  .sheet {
    position: relative;
    width: 876px;
    height: 1200px;
  }
  .postcard {
    position: absolute;
    left: 42px;
    width: 791px;
    box-shadow: 0 4px 14px rgba(0,0,0,.18);
    display: block;
  }
  .postcard--front { top: 60px; height: 519px; }
  .postcard--back  { top: 645px; height: 494px; }

  .brand-name   { font-family: "Libre Baskerville", serif; font-weight: 700; fill: var(--navy); }
  .tagline      { font-family: "Libre Baskerville", serif; font-weight: 700; fill: var(--navy); letter-spacing: 3px; }
  .claim        { font-family: "Yanone Kaffeesatz", sans-serif; fill: var(--paper); }
  .contact-head { font-family: "Libre Baskerville", serif; fill: var(--paper); letter-spacing: 1px; }
  .phone-number { font-family: "Kanit", sans-serif; font-weight: 500; fill: var(--ink); }
  .web-address  { font-family: "Libre Baskerville", serif; fill: var(--paper); letter-spacing: 3px; }
  .intro-head   { font-family: "Tinos", serif; font-weight: 700; fill: var(--paper); letter-spacing: 2px; }
  .intro-text   { font-family: "Libre Baskerville", serif; fill: var(--paper); }
  .package-head { font-family: "Tinos", serif; font-weight: 700; fill: var(--ink); letter-spacing: 1px; }
  .package-item { font-family: "Libre Baskerville", serif; fill: var(--ink); }
</style>
</head>
<body>
<main class="sheet">

  <!-- Vorderseite -->
  <svg class="postcard postcard--front" viewBox="0 0 1242 815" xmlns="http://www.w3.org/2000/svg">
    <defs>
      <linearGradient id="cityTone" x1="0" y1="0" x2="0" y2="1">
        <stop offset="0" stop-color="#dfe9f3"/>
        <stop offset="0.35" stop-color="#eef2f5"/>
        <stop offset="0.6" stop-color="#a9aeb6"/>
        <stop offset="1" stop-color="#7d7c80"/>
      </linearGradient>
      <radialGradient id="agentTone" cx="0.55" cy="0.5" r="0.7">
        <stop offset="0" stop-color="#3d7e95"/>
        <stop offset="0.5" stop-color="#20405a"/>
        <stop offset="1" stop-color="#16243a"/>
      </radialGradient>
      <linearGradient id="royalBand" x1="0" y1="0" x2="0" y2="1">
        <stop offset="0" stop-color="var(--royal)"/>
        <stop offset="1" stop-color="var(--royal-deep)"/>
      </linearGradient>
      <linearGradient id="pillFill" x1="0" y1="0" x2="0" y2="1">
        <stop offset="0" stop-color="#ffffff"/>
        <stop offset="1" stop-color="#cfcfd3"/>
      </linearGradient>
      <linearGradient id="silverRim" x1="0" y1="0" x2="1" y2="0">
        <stop offset="0" stop-color="#ffffff"/>
        <stop offset="1" stop-color="#a9a9b0"/>
      </linearGradient>
    </defs>

    <rect class="photo photo--skyline" role="img" aria-label="Foto: Stadtpanorama aus einem Hochhausfenster" width="1242" height="815" fill="url(#cityTone)"/>

    <path class="photo-rim" d="M445,0 H478 C600,110 625,420 545,610 L520,612 C600,420 575,110 445,0 Z" fill="url(#silverRim)"/>
    <path class="photo photo--agent" role="img" aria-label="Foto: Makler im Anzug mit geöffneten Händen unter einem leuchtenden Haussymbol" d="M0,0 H460 C585,110 605,410 522,612 L0,668 Z" fill="url(#agentTone)"/>

    <text class="claim" x="262" y="338" font-size="33" text-anchor="middle">Ihr komplettes Rundum-Paket erhalten Sie</text>
    <text class="claim" x="148" y="392" font-size="26" text-anchor="middle">alles aus</text>
    <text class="claim" x="330" y="410" font-size="62" text-anchor="middle">einer Hand</text>

    <text class="brand-name" x="1005" y="138" font-size="56" text-anchor="middle">NORDHAUS</text>
    <text class="tagline" x="1005" y="192" font-size="31" text-anchor="middle">We Love Real Estate</text>

    <path class="swoosh-rim" d="M0,668 C300,615 700,575 1242,600 V655 C900,590 400,600 0,668 Z" fill="#d4d4da"/>
    <path class="swoosh-line" d="M0,668 C400,600 900,590 1242,652" fill="none" stroke="#111" stroke-width="4"/>
    <path class="contact-band" d="M0,668 C400,602 900,592 1242,655 V765 H0 Z" fill="url(#royalBand)"/>

    <text class="contact-head" x="632" y="657" font-size="25" text-anchor="middle">Kontaktieren Sie uns</text>
    <rect class="phone-pill" x="337" y="675" width="581" height="50" rx="25" fill="url(#pillFill)"/>
    <g class="icon-phone" transform="translate(505,700)">
      <circle r="16" fill="none" stroke="var(--ink)" stroke-width="2.5"/>
      <path d="M-7,-8 l4,-2 l3,5 l-3,2 c1,4 3,6 6,7 l2,-3 l5,3 l-2,4 c-9,1 -16,-7 -15,-16 Z" fill="var(--ink)"/>
    </g>
    <text class="phone-number" x="655" y="712" font-size="34" text-anchor="middle">123-456-5678</text>

    <rect class="web-band" y="765" width="1242" height="50" fill="var(--band)"/>
    <text class="web-address" x="616" y="795" font-size="22" text-anchor="middle">www.website.com</text>
  </svg>

  <!-- Rückseite -->
  <svg class="postcard postcard--back" viewBox="0 0 1242 776" xmlns="http://www.w3.org/2000/svg">
    <defs>
      <linearGradient id="backRoyal" x1="0" y1="0" x2="1" y2="0.3">
        <stop offset="0" stop-color="var(--royal-deep)"/>
        <stop offset="0.6" stop-color="var(--royal)"/>
        <stop offset="1" stop-color="#0a0ad8"/>
      </linearGradient>
      <linearGradient id="panelFill" x1="0" y1="0" x2="0" y2="1">
        <stop offset="0" stop-color="#ffffff"/>
        <stop offset="1" stop-color="#d8d8db"/>
      </linearGradient>
      <linearGradient id="backPill" x1="0" y1="0" x2="0" y2="1">
        <stop offset="0" stop-color="#ffffff"/>
        <stop offset="1" stop-color="#cfcfd3"/>
      </linearGradient>
    </defs>

    <rect class="card-paper" width="1242" height="776" fill="var(--paper)"/>

    <path class="info-rim" d="M555,0 H575 C665,110 720,260 700,420 C685,560 650,660 610,726 H590 C630,660 665,560 680,420 C700,260 640,110 555,0 Z" fill="#e3e3ea"/>
    <path class="info-field" d="M0,0 H555 C640,110 700,260 680,420 C665,560 630,660 590,726 H0 Z" fill="url(#backRoyal)"/>

    <text class="intro-head" x="35" y="94" font-size="46">WIR BIETEN IHNEN</text>
    <text class="intro-text" font-size="20">
      <tspan x="35" y="132">ein echtes Rundum-Sorglos-Paket, bei dem Sie</tspan>
      <tspan x="35" y="154">alle Leistungen rund um Ihre Immobilie aus</tspan>
      <tspan x="35" y="176">einer einzigen Hand erhalten</tspan>
    </text>

    <path class="package-shadow" d="M660,530 L728,530 L690,548 Z" fill="#111"/>
    <path class="package-tab" d="M0,244 Q0,236 10,236 H380 Q395,236 405,250 L415,280 H0 Z" fill="var(--paper)"/>
    <rect class="package-panel" y="280" width="728" height="250" fill="url(#panelFill)"/>
    <text class="package-head" x="20" y="283" font-size="33">LEISTUNGSPAKET</text>

    <g class="package-list">
      <g fill="var(--navy)">
        <path d="M46,336 l14,6 l-14,6 l4,-6 Z"/>
        <path d="M46,361 l14,6 l-14,6 l4,-6 Z"/>
        <path d="M46,386 l14,6 l-14,6 l4,-6 Z"/>
        <path d="M46,436 l14,6 l-14,6 l4,-6 Z"/>
        <path d="M46,461 l14,6 l-14,6 l4,-6 Z"/>
      </g>
      <text class="package-item" font-size="20">
        <tspan x="77" y="349">Entrümpelung</tspan>
        <tspan x="77" y="374">Verkaufsgarantie</tspan>
        <tspan x="77" y="399">Wertsteigerung durch Renovierung mit eigenen</tspan>
        <tspan x="77" y="424">Handwerkern</tspan>
        <tspan x="77" y="449">Home Staging</tspan>
        <tspan x="77" y="474">und vieles mehr</tspan>
      </text>
    </g>

    <text class="contact-head" x="319" y="620" font-size="25" text-anchor="middle">Kontaktieren Sie uns</text>
    <rect class="phone-pill" x="87" y="640" width="478" height="44" rx="22" fill="url(#backPill)"/>
    <g class="icon-phone" transform="translate(189,662)">
      <circle r="15" fill="none" stroke="var(--ink)" stroke-width="2.5"/>
      <path d="M-7,-8 l4,-2 l3,5 l-3,2 c1,4 3,6 6,7 l2,-3 l5,3 l-2,4 c-9,1 -16,-7 -15,-16 Z" fill="var(--ink)"/>
    </g>
    <text class="phone-number" x="341" y="674" font-size="33" text-anchor="middle">123-456-5678</text>

    <text class="brand-name" x="668" y="92" font-size="40">NORDHAUS</text>

    <rect class="stamp-box" x="998.5" y="26.5" width="216" height="141" fill="none" stroke="#8a8a90" stroke-width="1.5"/>
    <g class="address-lines" stroke="var(--rule)" stroke-width="2">
      <line x1="750" y1="321" x2="1213" y2="321"/>
      <line x1="750" y1="373" x2="1213" y2="373"/>
      <line x1="750" y1="423" x2="1213" y2="423"/>
      <line x1="750" y1="475" x2="1213" y2="475"/>
    </g>

    <rect class="web-band" y="726" width="1242" height="50" fill="var(--band)"/>
    <text class="web-address" x="616" y="758" font-size="22" text-anchor="middle">www.website.com</text>
  </svg>

</main>
</body>
</html>
```